Need a fresh corporate identity for an existing Home Shopping Business in Thailand

We are one of the most active TV home shopping companies in Thailand. We need a fresh looking CI for our corporate, the colours of our corporate are Orange and Grey. We want our customers to see us as professional customer service who help them with their purchases.
The logo can be shown as a whole logo or either half logo but not less than half the logo.
Industry/Entity Type
Shopping
Requirements
Must have
- The logo should be shown at least half the logo or full logo.
Should not have
- The logo should not be shown less than half the logo.

```html
<!DOCTYPE html>
<html lang="en">
<head>
<meta charset="utf-8">
<title>Sunvale Home – Stationery Set</title>
<link href="https://fonts.googleapis.com/css2?family=Open+Sans:wght@400;600;700&display=swap" rel="stylesheet">
<style>
:root{
  --orange:#e4621f;
  --grey:#a9a9ad;
  --grey-dark:#8e8e93;
  --ink:#3a3a3c;
  --paper:#ffffff;
  --backdrop:#ececec;
}
*{margin:0;padding:0;box-sizing:border-box}
html,body{width:1200px;height:937px;overflow:hidden;background:var(--backdrop);font-family:"Open Sans",Arial,sans-serif;color:var(--ink)}
.canvas{position:relative;width:1200px;height:937px}
.sheet{position:absolute;background:var(--paper);overflow:hidden}
.band{position:absolute;left:0;width:100%;display:block}
.brand{display:flex;align-items:center;gap:6px;color:var(--orange);font-weight:600;white-space:nowrap}
.brand-dot{border-radius:50%;background:var(--orange);flex:none}

/* Letterhead front */
.letterhead{left:185px;top:66px;width:388px;height:546px}
.letterhead .brand{position:absolute;left:36px;top:88px;font-size:14px}
.letterhead .brand-dot{width:14px;height:14px}
.letter-body{position:absolute;left:36px;top:140px;width:300px;font-size:5.3px;line-height:7.4px;color:#555}
.letter-body p{margin-bottom:9px}
.letter-body .gap{margin-bottom:18px}
.signature{width:28px;height:12px;background:#444;opacity:.55;border-radius:6px;margin:4px 0 8px}
.contact-row{position:absolute;left:12px;right:12px;top:506px;display:flex;justify-content:space-between;font-size:6.3px;line-height:9px;font-weight:600;color:#444}
.contact-row div:last-child{text-align:right}

/* Letterhead back */
.letterhead-back{left:635px;top:40px;width:459px;height:576px}
.letterhead-back .brand{position:absolute;left:150px;top:350px;font-size:30px;font-weight:400}
.letterhead-back .brand-dot{width:26px;height:26px}
.site-on-band{position:absolute;left:0;width:100%;text-align:center;color:#fff;font-weight:600;letter-spacing:2px}
.letterhead-back .site-on-band{top:555px;font-size:11px}

/* Business cards */
.card{left:46px;width:175px;height:102px}
.card-front{top:655px}
.card-front .brand{position:absolute;left:6px;top:14px;font-size:8px}
.card-front .brand-dot{width:8px;height:8px}
.card-holder{position:absolute;right:8px;top:20px;text-align:right}
.card-holder .name{font-size:7px;font-weight:700;letter-spacing:.5px}
.card-holder .title{font-size:3.6px;color:#888;letter-spacing:.3px}
.card-contacts{position:absolute;left:4px;right:4px;top:75px;display:flex;justify-content:space-between;font-size:3.6px;line-height:5px}
.card-back{top:782px}
.card-back .brand{position:absolute;left:50%;top:44px;transform:translateX(-50%);font-size:11px}
.card-back .brand-dot{width:10px;height:10px}

/* Envelopes */
.envelope{top:671px;height:209px}
.envelope-front{left:265px;width:431px}
.envelope-front .brand{position:absolute;left:14px;top:104px;font-size:12px}
.envelope-front .brand-dot{width:12px;height:12px}
.envelope-front .site-on-band{top:193px;font-size:9px}
.envelope-back{left:737px;width:397px}
.flap{position:absolute;left:0;top:0;width:100%;height:95px;background:var(--grey);border-radius:0 0 40px 40px}
.flap-site{position:absolute;left:0;width:100%;top:28px;text-align:center;font-size:12px;letter-spacing:3px;font-weight:600;color:#333}
</style>
</head>
<body>
<main class="canvas">

  <!-- Letterhead front -->
  <section class="sheet letterhead">
    <div class="brand"><span class="brand-dot"></span>Sunvale Home</div>
    <div class="letter-body">
      <p>July 2, 2012</p>
      <p><strong>Dear Client,</strong><br>Lumen Building, 4 Garden St.</p>
      <p class="gap">Thank you for choosing our team for your home shopping needs. Our service staff stand ready to help you find the right products, answer questions about delivery and returns, and make every order simple from the first call to the moment it arrives.</p>
      <p class="gap">We are pleased to confirm your request and will contact you shortly with the details of your new account.</p>
      <p>Our programmes air every day with fresh offers for the home, kitchen and family. Should you need any help, please call our customer line or write to us, and a member of our team will gladly assist you with your purchase.</p>
      <p>Best Regards,</p>
      <div class="signature" role="img" aria-label="Handwritten signature"></div>
      <p><strong>Arin Wong</strong><br>Director<br><br>Lumen Building, 4 Garden St.</p>
    </div>
    <svg class="band" style="top:489px;height:15px" viewBox="0 0 388 15" preserveAspectRatio="none">
      <polygon points="0,0 120,0 128,7.5 120,15 0,15" fill="var(--grey)"/>
      <polygon points="124,0 276,0 284,7.5 276,15 124,15 132,7.5" fill="var(--grey)"/>
      <polygon points="280,0 388,0 388,15 280,15 288,7.5" fill="var(--grey)"/>
      <g fill="none" stroke="#555" stroke-width="1">
        <circle cx="48" cy="7.5" r="3.5"/><line x1="44.5" y1="7.5" x2="51.5" y2="7.5"/><ellipse cx="48" cy="7.5" rx="1.5" ry="3.5"/>
        <rect x="337" y="3.5" width="4" height="8" rx="1"/>
      </g>
      <path d="M202 3.5a2.5 2.5 0 0 1 2.5 2.5c0 2-2.5 5-2.5 5s-2.5-3-2.5-5a2.5 2.5 0 0 1 2.5-2.5z" fill="#555"/>
    </svg>
    <div class="contact-row">
      <div>hello@sunvalehome.com<br>www.sunvalehome.com</div>
      <div>27 Rama Tower<br>Sukhumvit Rd</div>
      <div>021 480 5530<br>021 480 5530</div>
    </div>
    <div class="band" style="top:533px;height:13px;background:var(--orange)"></div>
  </section>

  <!-- Letterhead back -->
  <section class="sheet letterhead-back">
    <svg class="band" style="top:0;height:25px" viewBox="0 0 459 25" preserveAspectRatio="none">
      <polygon points="0,0 122,0 130,12.5 122,25 0,25" fill="var(--grey)"/>
      <polygon points="128,0 350,0 358,12.5 350,25 128,25 136,12.5" fill="var(--grey)"/>
      <polygon points="356,0 459,0 459,25 356,25 364,12.5" fill="var(--grey)"/>
    </svg>
    <div class="brand"><span class="brand-dot"></span>Sunvale Home</div>
    <svg class="band" style="top:549px;height:27px" viewBox="0 0 459 27" preserveAspectRatio="none">
      <polygon points="0,0 110,0 102,13.5 110,27 0,27" fill="var(--orange)"/>
      <polygon points="114,0 340,0 332,13.5 340,27 114,27 106,13.5" fill="var(--orange)"/>
      <polygon points="344,0 459,0 459,27 344,27 336,13.5" fill="var(--orange)"/>
    </svg>
    <div class="site-on-band">www.sunvalehome.com</div>
  </section>

  <!-- Business card front -->
  <section class="sheet card card-front">
    <div class="brand"><span class="brand-dot"></span>Sunvale Home</div>
    <div class="card-holder"><div class="name">DANA REYES</div><div class="title">CORPORATE TITLE</div></div>
    <svg class="band" style="top:59px;height:12px" viewBox="0 0 175 12" preserveAspectRatio="none">
      <polygon points="0,0 54,0 58,6 54,12 0,12" fill="var(--grey)"/>
      <polygon points="56,0 112,0 116,6 112,12 56,12 60,6" fill="var(--grey)"/>
      <polygon points="114,0 175,0 175,12 114,12 118,6" fill="var(--grey)"/>
      <circle cx="22" cy="6" r="3" fill="none" stroke="#555" stroke-width=".8"/>
      <path d="M84 3a2 2 0 0 1 2 2c0 1.6-2 4-2 4s-2-2.4-2-4a2 2 0 0 1 2-2z" fill="#555"/>
      <rect x="148" y="3" width="3.5" height="6.5" rx=".8" fill="none" stroke="#555" stroke-width=".8"/>
    </svg>
    <div class="card-contacts">
      <div>hello@sunvalehome.com<br>www.sunvalehome.com</div>
      <div>27 Rama Tower<br>Sukhumvit Rd</div>
      <div>021 480 5530<br>021 480 5530</div>
    </div>
  </section>

  <!-- Business card back -->
  <section class="sheet card card-back">
    <svg class="band" style="top:0;height:10px" viewBox="0 0 175 10" preserveAspectRatio="none">
      <polygon points="0,0 56,0 60,5 56,10 0,10" fill="var(--grey)"/>
      <polygon points="58,0 132,0 136,5 132,10 58,10 62,5" fill="var(--grey)"/>
      <polygon points="134,0 175,0 175,10 134,10 138,5" fill="var(--grey)"/>
    </svg>
    <div class="brand"><span class="brand-dot"></span>Sunvale Home</div>
    <svg class="band" style="top:92px;height:10px" viewBox="0 0 175 10" preserveAspectRatio="none">
      <polygon points="0,0 40,0 36,5 40,10 0,10" fill="var(--orange)"/>
      <polygon points="42,0 128,0 124,5 128,10 42,10 38,5" fill="var(--orange)"/>
      <polygon points="130,0 175,0 175,10 130,10 126,5" fill="var(--orange)"/>
    </svg>
  </section>

  <!-- Envelope front -->
  <section class="sheet envelope envelope-front">
    <svg class="band" style="top:0;height:20px" viewBox="0 0 431 20" preserveAspectRatio="none">
      <polygon points="0,0 112,0 118,10 112,20 0,20" fill="var(--grey)"/>
      <polygon points="116,0 326,0 332,10 326,20 116,20 122,10" fill="var(--grey)"/>
      <polygon points="330,0 431,0 431,20 330,20 336,10" fill="var(--grey)"/>
    </svg>
    <div class="brand"><span class="brand-dot"></span>Sunvale Home</div>
    <svg class="band" style="top:189px;height:20px" viewBox="0 0 431 20" preserveAspectRatio="none">
      <polygon points="0,0 104,0 98,10 104,20 0,20" fill="var(--orange)"/>
      <polygon points="108,0 312,0 306,10 312,20 108,20 102,10" fill="var(--orange)"/>
      <polygon points="316,0 431,0 431,20 316,20 310,10" fill="var(--orange)"/>
    </svg>
    <div class="site-on-band">www.sunvalehome.com</div>
  </section>

  <!-- Envelope back -->
  <section class="sheet envelope envelope-back">
    <div class="flap"></div>
    <div class="flap-site">www.sunvalehome.com</div>
  </section>

</main>
</body>
</html>
```